Restaurant, Nightclub

It's a Restaurant come nightclub. Our sign Tamsel is white letters with blue edging on a black back ground.

Industry/Entity Type

Restaurant

Contact Information for Business Card

Tamsel Stevenage Ltd
14 Larkfield Row
Quillbury Norvs KX7 2PW

```html
<!DOCTYPE html>
<html lang="en">
<head>
<meta charset="utf-8">
<title>Tamsel Quillbury Ltd – Business Card</title>
<link href="https://fonts.googleapis.com/css2?family=Michroma&display=swap" rel="stylesheet">
<style>
  :root {
    --backdrop: #1d1d1f;
    --brick-deep: #6e2f17;
    --brick-warm: #b5562a;
    --brick-light: #c9733f;
    --paving-light: #c79a86;
    --paving-mid: #a87a68;
    --paving-dark: #8a6152;
    --sign-black: #0b0b0c;
    --sign-frame: #2a2a2a;
    --sign-letter: #b9bcc0;
    --ink: #0e0e0e;
  }
  * { margin: 0; padding: 0; box-sizing: border-box; }
  html, body {
    width: 1200px;
    height: 900px;
    overflow: hidden;
    background: var(--backdrop);
  }
  .canvas {
    position: relative;
    width: 1200px;
    height: 900px;
    display: flex;
    align-items: center;
    justify-content: center;
  }
  .business-card {
    position: relative;
    width: 1000px;
    height: 600px;
    overflow: hidden;
    box-shadow: 0 20px 50px rgba(0,0,0,0.6);
    font-family: "Michroma", sans-serif;
  }
  .brick-wall {
    position: absolute;
    inset: 0 0 38% 0;
    background:
      radial-gradient(ellipse at 70% 35%, var(--brick-light) 0%, transparent 60%),
      linear-gradient(160deg, var(--brick-warm) 0%, var(--brick-deep) 100%);
  }
  .paving-band {
    position: absolute;
    left: 0; right: 0; bottom: 0;
    height: 38%;
    background: linear-gradient(170deg, var(--paving-mid) 0%, var(--paving-light) 45%, var(--paving-dark) 100%);
  }
  .sign-panel {
    position: absolute;
    left: 11%;
    top: 9%;
    width: 83%;
    height: 46%;
    background: var(--sign-black);
    border: 8px solid var(--sign-frame);
    outline: 2px solid #000;
    display: flex;
    align-items: center;
    justify-content: center;
  }
  .sign-name {
    color: var(--sign-letter);
    font-size: 150px;
    font-weight: 400;
    letter-spacing: 0.02em;
    line-height: 1;
  }
  .card-details {
    position: absolute;
    left: 20%;
    right: 3%;
    bottom: 12%;
    color: var(--ink);
    font-variant: small-caps;
  }
  .company-name {
    font-size: 42px;
    font-weight: 400;
    letter-spacing: 0.14em;
    line-height: 1.1;
    white-space: nowrap;
  }
  .company-address {
    margin-top: 12px;
    margin-left: 70px;
    font-size: 19px;
    letter-spacing: 0.14em;
    white-space: nowrap;
  }
</style>
</head>
<body>
  <main class="canvas">
    <section class="business-card">
      <div class="brick-wall" role="img" aria-label="Weathered orange-red brick wall texture"></div>
      <div class="paving-band" role="img" aria-label="Pale pink-beige brickwork texture"></div>
      <div class="sign-panel">
        <span class="sign-name">Tamsel</span>
      </div>
      <div class="card-details">
        <h1 class="company-name">Tamsel Quillbury Ltd</h1>
        <p class="company-address">14 Larkfield Row Quillbury Norvs KX7 2PW</p>
      </div>
    </section>
  </main>
</body>
</html>
```